Brochure for Specialist Divorce Support

1. I want an A4 three fold brochure or DL to promote my business and services.
My market are people going through divorce and are usually feeling very overwhelmed and therefore not functioning very well - both men and women, age early forties,
2. Colours – variety of blues and lime greens but you choose if you need a contrast e.g. orange
3. Images – happy single families
4. Theme - could you make it around water please - soothing
5. Logos – HWN &; HWT (I will attach)
6. I have a lot of content so maybe not too busy but still professional feel +
warm and reassuring
7. I'm attaching -

- a draft brochure I put together using a Microsoft template
- a word document with extra details
- plus two logos to do with my qualifications
- and some images for you to choose from

7. I want to use this as a template for some other brochures -> more work for
the winner.

Target Market(s)

Men and women usually in their early forties with primary school aged children i.e 5 to 12 years old.
They are going through a divorce and very upset, Maybe losing contact with their children and their way of life as they know it is disappearing. They are in turmoil and not functioning as well as they usually do.

Industry/Entity Type

Business

Font styles to use
Sans Serif

Colors
34a7d7
abd037
3277b5

Requirements
Must have
• I want the brochure to be three folds with the center the full A4
• Could you make the theme around water please.
• I will upload some photos for you to use if you want,

```html
<!DOCTYPE html>
<html lang="en">
<head>
<meta charset="utf-8">
<title>Tailored Divorce Support – Tri-fold Brochure</title>
<link href="https://fonts.googleapis.com/css2?family=Oswald:wght@500;600&family=Montserrat:wght@400;500;600;700;800&display=swap" rel="stylesheet">
<style>
  :root{
    --navy:#1f3373;
    --navy-deep:#172a63;
    --blue:#34a7d7;
    --blue-mid:#3277b5;
    --lime:#abd037;
    --ink:#3a3f4a;
    --paper:#ffffff;
    --paper-shade:#eef0f2;
    --stage:#e6e7e9;
  }
  *{box-sizing:border-box;margin:0;padding:0}
  html,body{width:1200px;height:880px;overflow:hidden;background:var(--stage)}
  body{font-family:"Montserrat",sans-serif;color:var(--ink)}
  .brochure{position:relative;width:1200px;height:880px;display:flex}
  .panel{position:relative;width:400px;height:880px;overflow:hidden}

  /* shared heading */
  .section-head{position:absolute;left:22px;right:0;display:flex;align-items:center;gap:14px;z-index:2}
  .section-head .badge{width:62px;height:62px;border-radius:50%;background:var(--lime);border:4px solid var(--paper);box-shadow:0 0 0 2px var(--lime);display:flex;align-items:center;justify-content:center;flex:none}
  .section-head h2{font-family:"Oswald",sans-serif;font-weight:600;font-size:40px;letter-spacing:.5px;line-height:1}
  .section-rule{position:absolute;height:2px}

  /* left panel */
  .panel--services{background:linear-gradient(90deg,var(--paper) 0%,var(--paper) 75%,var(--paper-shade) 100%)}
  .panel--services h2{color:var(--blue-mid)}
  .services-list{position:absolute;left:26px;right:22px;top:124px;list-style:none}
  .services-list li{display:flex;gap:10px;font-size:11px;line-height:1.5;margin-bottom:10px}
  .services-list svg{flex:none;margin-top:1px}
  .testimonial{position:absolute;left:36px;right:28px;top:440px;font-size:11px;line-height:1.65;text-align:justify}
  .testimonial .mark{font-family:Georgia,serif;font-size:24px;color:#9aa0a8;line-height:.6;font-weight:700;display:block;height:12px}
  .testimonial .mark--close{display:inline-block;height:auto;margin-left:8px;vertical-align:-8px}
  .signature{position:absolute;left:0;width:330px;top:628px;text-align:center}
  .signature .name{font-weight:700;font-size:26px;line-height:1.15;color:var(--blue-mid);letter-spacing:1px}
  .signature .role{font-size:14px;line-height:1.2;color:var(--blue)}
  .photo-meadow{position:absolute;left:0;top:690px;width:400px;height:190px;background:radial-gradient(ellipse at 40% 70%,#c89d7c 0%,#8fa65a 35%,#6f8f3a 70%,#5d7a2c 100%)}
  .meadow-curve{position:absolute;left:0;top:688px;width:400px;height:80px;z-index:1}

  /* middle panel */
  .panel--quotes{background:linear-gradient(180deg,var(--navy-deep) 0%,#2a4796 100%)}
  .panel--quotes h2{color:var(--lime)}
  .quotes{position:absolute;left:22px;right:26px;top:112px;color:#fff;list-style:none}
  .quotes li{position:relative;padding-left:16px;font-size:11px;line-height:1.6;margin-bottom:10px;text-align:justify}
  .quotes li::before{content:"—";position:absolute;left:-4px;top:0}
  .contact{position:absolute;left:30px;top:504px;color:#fff;list-style:none}
  .contact li{display:flex;align-items:center;gap:10px;font-size:13px;line-height:1.2;margin-bottom:9px}
  .contact li.strong{font-weight:700}
  .contact svg{flex:none}
  .photo-beach{position:absolute;left:82px;top:590px;width:228px;height:228px;border-radius:50%;border:7px solid var(--blue);box-shadow:0 0 0 4px var(--paper);background:linear-gradient(180deg,#9fc9ea 0%,#cfe3f0 45%,#7fb2cf 55%,#d9cdb8 100%);z-index:2}
  .wave-bottom{position:absolute;left:0;bottom:0;width:400px;height:180px}
  .site-link{position:absolute;left:0;width:400px;bottom:24px;text-align:center;font-size:13.5px;color:var(--navy);z-index:3}

  /* right panel */
  .panel--cover{background:var(--paper)}
  .brand{position:absolute;left:0;right:0;top:52px;display:flex;align-items:center;justify-content:center;gap:14px}
  .brand .dot{width:26px;height:26px;border-radius:50%;background:#c8202f}
  .brand .name{font-weight:800;font-size:64px;color:#c8202f;letter-spacing:2px;line-height:1}
  .brand--second{top:148px}
  .brand--second .square{width:20px;height:20px;background:var(--navy)}
  .brand--second .name{font-size:42px;color:var(--navy);font-weight:800}
  .photo-family{position:absolute;left:0;top:222px;width:400px;height:470px;background:radial-gradient(ellipse at 45% 40%,#e6c6a8 0%,#c9a68a 30%,#9fae7a 65%,#7f9a5a 100%)}
  .cover-band{position:absolute;left:0;bottom:0;width:400px;height:240px}
  .cover-title{position:absolute;left:0;width:400px;top:700px;text-align:center;font-weight:700;line-height:1.05}
  .cover-title .lime{color:var(--lime);font-size:34px;display:block}
  .cover-title .white{color:#fff;font-size:35px;display:block;letter-spacing:.5px}
  .cover-title hr{width:320px;margin:6px auto 0;border:0;border-top:1px solid rgba(255,255,255,.7)}
  .cover-sub{position:absolute;left:30px;right:30px;top:786px;text-align:center;color:#fff;font-size:10.5px;line-height:1.5}
  .cover-pill{position:absolute;left:90px;top:824px;width:210px;height:44px;border-radius:10px 10px 0 0;background:var(--paper);display:flex;align-items:center;justify-content:center;font-size:13px;color:var(--navy)}
</style>
</head>
<body>
<main class="brochure">

  <section class="panel panel--services">
    <header class="section-head" style="top:30px">
      <span class="badge">
        <svg width="32" height="32" viewBox="0 0 32 32" fill="none" stroke="#fff" stroke-width="2.4"><circle cx="16" cy="13" r="6"/><path d="M16 3v3M16 20v3M6 13h3M23 13h3M9 6l2 2M21 18l2 2M23 6l-2 2M11 18l-2 2"/><path d="M4 27h10l8-3"/></svg>
      </span>
      <h2>MY SERVICES</h2>
    </header>
    <svg class="section-rule" style="left:100px;top:96px;width:300px;height:12px" viewBox="0 0 300 12"><path d="M0 11 Q150 8 300 1" stroke="#abd037" stroke-width="2" fill="none"/></svg>

    <ul class="services-list">
      <li><svg width="15" height="15" viewBox="0 0 16 16" fill="none" stroke="#3277b5" stroke-width="1.8"><circle cx="8" cy="8" r="6.5"/><path d="M4.5 8l2.5 2.5L14 2"/></svg>Specialist divorce support to suit your needs.</li>
      <li><svg width="15" height="15" viewBox="0 0 16 16" fill="none" stroke="#3277b5" stroke-width="1.8"><circle cx="8" cy="8" r="6.5"/><path d="M4.5 8l2.5 2.5L14 2"/></svg>Pre-mediation coaching helping you prepare and achieve more positive outcomes to avoid going to court</li>
      <li><svg width="15" height="15" viewBox="0 0 16 16" fill="none" stroke="#3277b5" stroke-width="1.8"><circle cx="8" cy="8" r="6.5"/><path d="M4.5 8l2.5 2.5L14 2"/></svg>Collaborative law coaching to increase crucial skills so you can participate more constructively in negotiations</li>
      <li><svg width="15" height="15" viewBox="0 0 16 16" fill="none" stroke="#3277b5" stroke-width="1.8"><circle cx="8" cy="8" r="6.5"/><path d="M4.5 8l2.5 2.5L14 2"/></svg>Delivery of HWN Clear Path Profile giving you real feedback on the constructive and destructive behaviours you choose during conflict situations to facilitate more productive discussions</li>
      <li><svg width="15" height="15" viewBox="0 0 16 16" fill="none" stroke="#3277b5" stroke-width="1.8"><circle cx="8" cy="8" r="6.5"/><path d="M4.5 8l2.5 2.5L14 2"/></svg>Corporate Conflict Management Training</li>
    </ul>

    <header class="section-head" style="top:352px">
      <span class="badge">
        <svg width="30" height="30" viewBox="0 0 30 30" fill="none" stroke="#fff" stroke-width="2.2"><path d="M4 5h16v11H10l-5 4v-4H4z"/><path d="M14 19v3h8l4 4v-4h1V12h-4"/></svg>
      </span>
      <h2>TESTIMONIAL</h2>
    </header>
    <svg class="section-rule" style="left:100px;top:418px;width:300px;height:4px" viewBox="0 0 300 4"><path d="M0 2H300" stroke="#abd037" stroke-width="2"/></svg>

    <div class="testimonial">
      <span class="mark">“</span>
      <p>After many cups of coffee and long hours of listening to me, my very good friend suggested I speak to Marianne, a divorce coach. I was a bit skeptical, especially when a phone session was suggested.</p>
      <p>From my first phone session I felt empowered. It gave me a sense of direction, assisted me to set realistic goals and action plans. Most importantly it aided my self esteem. Divorce is overwhelming. Talking to a caring professional like Marianne helped me acknowledge my priorities and a way to achieve them. Thank you Marianne.<span class="mark mark--close">”</span></p>
    </div>

    <div class="signature">
      <div class="name">MARISOL</div>
      <div class="role">Ccccccc, Smmmmm. AAA</div>
    </div>

    <div class="photo-meadow" role="img" aria-label="Photo of a mother and young son cuddling in a sunny grass meadow"></div>
    <svg class="meadow-curve" viewBox="0 0 400 80" preserveAspectRatio="none">
      <path d="M0 0 L400 0 L400 72 Q200 30 0 4 Z" fill="#f4f5f6"/>
      <path d="M0 4 Q200 30 400 72" stroke="#abd037" stroke-width="4" fill="none"/>
    </svg>
  </section>

  <section class="panel panel--quotes">
    <header class="section-head" style="top:30px">
      <span class="badge">
        <svg width="30" height="30" viewBox="0 0 30 30"><ellipse cx="15" cy="13" rx="12" ry="9" fill="#fff"/><path d="M8 20l-2 6 7-4z" fill="#fff"/><text x="15" y="19" text-anchor="middle" font-family="Georgia,serif" font-size="17" font-weight="700" fill="#abd037">”</text></svg>
      </span>
      <h2>SOME QUOTES</h2>
    </header>
    <svg class="section-rule" style="left:92px;top:96px;width:308px;height:12px" viewBox="0 0 308 12"><path d="M0 11 Q160 8 308 1" stroke="#fff" stroke-width="1.5" fill="none"/></svg>

    <ul class="quotes">
      <li>Often family and friends can try to influence decisions based on what they see as best, so you can feel under an enormous pressure to keep them happy. Coaching offers an objective and neutral sounding board there just for you.</li>
      <li>Even the most together person can be totally unprepared for the emotional overwhelm that divorce can bring, regardless if they are the one who made the decision to leave.</li>
      <li>Every divorce is different and families going forward will be different. I try to get my client to see or find ways they can co-parent as opposed to being one of two single parents.</li>
      <li>Everyone is different and move through these stages at their own pace</li>
    </ul>

    <header class="section-head" style="top:422px">
      <span class="badge">
        <svg width="32" height="32" viewBox="0 0 32 32" fill="none" stroke="#fff" stroke-width="2.2"><path d="M5 6c2-2 4-2 5 0l2 4-3 3c1 3 3 5 6 6l3-3 4 2c2 1 2 3 0 5-3 3-10 0-14-4S2 9 5 6z"/><rect x="16" y="14" width="13" height="9"/><path d="M16 14l6.5 5 6.5-5"/></svg>
      </span>
      <h2>CONTACT US</h2>
    </header>
    <svg class="section-rule" style="left:92px;top:482px;width:308px;height:4px" viewBox="0 0 308 4"><path d="M0 2H308" stroke="#fff" stroke-width="1.5"/></svg>

    <ul class="contact">
      <li><svg width="12" height="14" viewBox="0 0 12 14"><path d="M6 0a5 5 0 0 1 5 5c0 4-5 9-5 9S1 9 1 5a5 5 0 0 1 5-5z" fill="#abd037"/><circle cx="6" cy="5" r="2" fill="#1f3373"/></svg>Address Goes Here</li>
      <li class="strong"><svg width="13" height="13" viewBox="0 0 13 13"><circle cx="6.5" cy="6.5" r="6.5" fill="#abd037"/><path d="M4 3.5l1.5 2-1 1c.5 1 1.3 1.8 2.3 2.3l1-1 2 1.5-1 1.2C6 10 3 7 2.8 4.5z" fill="#1f3373"/></svg>+123 456 7890 &nbsp;|&nbsp; +123 457 8900</li>
      <li class="strong"><svg width="13" height="10" viewBox="0 0 13 10"><rect width="13" height="10" fill="#abd037"/><path d="M0 0l6.5 5L13 0" stroke="#1f3373" fill="none"/></svg>info@emailaddress.com</li>
    </ul>

    <div class="photo-beach" role="img" aria-label="Photo of a mother and two children walking together along a sunny beach shoreline"></div>

    <svg class="wave-bottom" viewBox="0 0 400 180" preserveAspectRatio="none">
      <path d="M0 70 Q200 40 400 20 L400 180 L0 180Z" fill="#3277b5"/>
      <path d="M0 82 Q200 58 400 44 L400 180 L0 180Z" fill="#abd037"/>
    </svg>
    <div class="site-link">www.websiteaddress.com</div>
  </section>

  <section class="panel panel--cover">
    <div class="brand">
      <span class="dot"></span>
      <span class="name">HWN</span>
    </div>
    <div class="brand brand--second">
      <span class="square"></span>
      <span class="name">HWT</span>
    </div>

    <div class="photo-family" role="img" aria-label="Photo of a smiling mother hugging her young daughter outdoors in soft sunlight"></div>

    <svg class="cover-band" viewBox="0 0 400 240" preserveAspectRatio="none">
      <path d="M0 52 Q180 -5 400 40 L400 240 L0 240Z" fill="#abd037"/>
      <path d="M0 78 Q190 18 400 66 L400 240 L0 240Z" fill="#1f3373"/>
    </svg>
    <h1 class="cover-title">
      <span class="lime">TAILORED</span>
      <span class="white">DIVORCE SUPPORT</span>
      <hr>
    </h1>
    <p class="cover-sub">Helping you move through this major life challenge so you can more successfully start living your new life – your way!</p>
    <div class="cover-pill">www.websiteaddress.com</div>
  </section>

</main>
</body>
</html>
```